Castlewood Trading Company need a book cover designing. The book is called "Gather M...

Please submit it as a jpg at 300 dpi with A5 dimensions (14.8 cm wide by 21 cm high), and make sure that your text is well within the trim line - approximately 2 cm from the edge. We like the style "Gather" is written in the attached image, although this is a guideline. It CANNOT be copied, but it may provide influence and inspiration. We are looking for a crisp and clean book cover, so probably on a white background.Our Logo is also attached and we see this being included centered at the bottom "There is a better way to grow your savings" is what the book is about

```html
<!DOCTYPE html>
<html lang="en">
<head>
<meta charset="utf-8">
<title>Gather Mill – Book Cover</title>
<link rel="stylesheet" href="https://fonts.googleapis.com/css2?family=Caveat+Brush&family=PT+Sans:ital,wght@0,700;1,400;1,700&display=swap">
<style>
  :root {
    --backdrop: #c9d0d0;
    --paper: #ffffff;
    --leaf-green: #5b8c2f;
    --jar-light: #f1f3f2;
    --jar-mid: #d9dcd8;
    --coin-tone: #b8aa98;
  }
  html, body {
    margin: 0;
    padding: 0;
    width: 1200px;
    height: 989px;
    overflow: hidden;
    background: var(--backdrop);
  }
  .canvas {
    position: relative;
    width: 1200px;
    height: 989px;
  }
  .book-cover {
    position: absolute;
    left: 283px;
    top: 44px;
    width: 634px;
    height: 900px;
    background: var(--paper);
    box-shadow: 0 2px 10px rgba(0,0,0,0.12);
    overflow: hidden;
  }
  .title {
    position: absolute;
    left: 0;
    right: 0;
    top: 100px;
    margin: 0;
    text-align: center;
    font-family: "Caveat Brush", cursive;
    font-weight: 400;
    font-size: 168px;
    line-height: 0.78;
    color: var(--leaf-green);
    transform: rotate(-2deg);
  }
  .title span { display: block; }
  .savings-photo {
    position: absolute;
    left: 96px;
    top: 462px;
    width: 510px;
    height: 275px;
    background: linear-gradient(180deg, var(--paper) 0%, var(--jar-light) 35%, var(--jar-mid) 70%, var(--coin-tone) 100%);
    border-radius: 4px;
  }
  .tagline {
    position: absolute;
    left: 265px;
    top: 448px;
    margin: 0;
    font-family: "PT Sans", sans-serif;
    font-style: italic;
    font-size: 18px;
    line-height: 1.25;
    color: var(--leaf-green);
    letter-spacing: -0.3px;
  }
  .tagline strong { font-weight: 700; }
  .author {
    position: absolute;
    left: 0;
    right: 0;
    top: 750px;
    margin: 0;
    text-align: center;
    font-family: "PT Sans", sans-serif;
    font-weight: 700;
    font-size: 52px;
    color: var(--leaf-green);
    letter-spacing: -0.5px;
  }
</style>
</head>
<body>
  <main class="canvas">
    <section class="book-cover">
      <h1 class="title"><span>Gather</span><span>Mill</span></h1>
      <div class="savings-photo" role="img" aria-label="Row of four glass jars filling with coins, a green seedling growing from each fuller jar"></div>
      <p class="tagline">There is <strong>a better way</strong><br>to <strong>grow</strong> your savings</p>
      <p class="author">Author Name</p>
    </section>
  </main>
</body>
</html>
```